Social Media Marketing Website

I would like someone to finish off my website as the previous designer has decided otherwise. I like the current layout but it can be better. I also want the site to reflect my portfolio uploaded on each brand I have worked with. I need to upload videos and make the website responsive and load very quickly. It also needs to be mobile and tablet friendly. I know my way around websites and what is current. my website is www.pkdnorthly.com

Target Market(s)

Business seeking brand consultation and ecommerce solutions

Industry/Entity Type

Digital Marketing

Coding

Coded - Design and coding required

Number of Pages Required

5+ page

Font styles to use
Other font styles liked:
• Bebas Neue

Colors
ffffff
aaaaaa
f5f5f5
fffbf0

Requirements
Must have
• Fast loading website that is easy to navigate. Can withstand video content and high res pictures. Easy backend to operate. Google Analytics Set Up.
Nice to have
• Interactive site
Should not have
• Complex design that is not easy to navigate for the non tech savvy visitor.

```html
<!DOCTYPE html>
<html lang="en">
<head>
<meta charset="utf-8">
<title>Parkdale Northly – Social Media Marketing</title>
<link href="https://fonts.googleapis.com/css2?family=Montserrat:wght@400;600;700;800&family=Open+Sans:wght@600;700&display=swap" rel="stylesheet">
<style>
:root{
  --navy:#27313d;
  --navy-deep:#1f2833;
  --ink:#1c242e;
  --white:#ffffff;
  --panel:#f0f0f0;
  --field:#eeeeee;
  --grey:#aaaaaa;
  --muted:#c9ced4;
}
*{margin:0;padding:0;box-sizing:border-box}
html,body{width:1200px;height:2932px;overflow:hidden}
body{font-family:"Open Sans",Arial,sans-serif;color:var(--ink);background:var(--white);position:relative}
.abs{position:absolute}
.head{font-family:"Montserrat",Arial,sans-serif}
p.small{font-size:12.5px;font-weight:700;line-height:16px}

/* hero */
.hero{position:absolute;left:0;top:0;width:1200px;height:571px;background:var(--navy);color:var(--white)}
.topbar{position:absolute;left:0;top:0;width:1200px;height:43px;border-bottom:1px solid #3a4551;font-size:12px;font-weight:700}
.topbar span{position:absolute;top:13px}
.social{position:absolute;display:flex;gap:18px}
.social i{display:block;width:10px;height:10px;border-radius:50%;background:var(--white)}
.brand{position:absolute;background:var(--white);border:3px solid #d8d8d8;display:flex;align-items:center;justify-content:center;text-align:center;font-family:"Montserrat",Arial,sans-serif;font-weight:600;color:var(--ink);line-height:14px;font-size:12px}
.nav{position:absolute;display:flex;gap:30px;font-family:"Montserrat",Arial,sans-serif;font-weight:700;font-size:12px}
.hero-art{position:absolute;left:680px;top:147px;width:454px;height:351px;background:radial-gradient(ellipse at center,#3a4652 0%,#2c3744 70%,var(--navy) 100%);border-radius:20px}
.hero h1{position:absolute;left:86px;top:206px;z-index:2;white-space:nowrap;font-family:"Montserrat",Arial,sans-serif;font-weight:400;font-size:38px;line-height:48px}
.hero h1 .strong{font-weight:800;font-size:48px}
.hero h1 .line2{font-weight:700;font-size:35px;letter-spacing:-0.3px}
.discover{position:absolute;left:86px;top:320px;border-left:3px solid var(--white);padding-left:10px}
.discover h3{font-family:"Montserrat",Arial,sans-serif;font-size:19px;font-weight:700}
.btn{position:absolute;height:45px;display:flex;align-items:center;justify-content:center;font-family:"Montserrat",Arial,sans-serif;font-weight:700;font-size:11px}
.btn.light{background:#e9e9e9;color:var(--ink)}
.btn.ghost{border:2px solid var(--white);color:var(--white)}
.dots{position:absolute;left:555px;top:524px;width:90px;height:25px;background:var(--white);border-radius:13px;display:flex;align-items:center;justify-content:center;gap:5px}
.dots i{width:9px;height:9px;border-radius:50%;border:2px solid var(--navy)}
.dots i.on{background:var(--navy)}

/* services */
.section-title{position:absolute;font-family:"Montserrat",Arial,sans-serif;font-size:26px;font-weight:400}
.section-title b{font-weight:800}
.rule{position:absolute;height:1px;background:var(--grey)}
.service{position:absolute;top:688px;width:240px}
.service svg{height:48px}
.service h4{font-family:"Montserrat",Arial,sans-serif;font-size:12.5px;font-weight:800;margin:14px 0 6px}

/* offer */
.offer-band{position:absolute;left:0;top:840px;width:1200px;height:338px}
.lead{position:absolute;left:0;width:1200px;text-align:center;color:var(--white);font-family:"Montserrat",Arial,sans-serif}
.offer{position:absolute;left:166px;top:995px;width:868px;height:151px;background:var(--white);border:3px solid #d7d7d7}

/* work */
.photo{position:absolute;background:linear-gradient(160deg,#4a4a4a,#1a1a1a 70%)}
.work-panel{position:absolute;left:500px;top:1243px;width:616px;height:501px;background:var(--panel)}
.work-panel h4{font-family:"Montserrat",Arial,sans-serif;font-size:14px;font-weight:800;margin-bottom:8px}
.arrows{position:absolute;display:flex;gap:4px}
.arrows i{width:32px;height:32px;display:flex;align-items:center;justify-content:center;font-style:normal;font-size:15px;font-weight:700}

/* videos */
.videos{position:absolute;left:0;top:1814px;width:1200px;height:545px;background:var(--navy);color:var(--white)}
.video{position:absolute;top:108px;width:326px}
.thumb{height:164px;position:relative;border:2px solid var(--white)}
.thumb em{position:absolute;right:4px;bottom:6px;background:#111;color:#fff;font-style:normal;font-size:11px;font-weight:700;padding:4px 8px}
.video h4{font-family:"Montserrat",Arial,sans-serif;font-size:12.5px;font-weight:800;margin:22px 0 6px}

/* footer */
.footer{position:absolute;left:0;top:2604px;width:1200px;height:328px;background:var(--navy-deep);color:var(--white)}
</style>
</head>
<body>

<header class="hero">
  <div class="topbar">
    <span style="left:86px">CALL: &nbsp;XXX XXX XXXX</span>
    <span style="left:348px">MAIL: &nbsp;<span style="position:static;font-weight:600">hello@parkdalenorthly.com</span></span>
    <div class="social" style="left:955px;top:16px"><i></i><i></i><i></i><i></i><i></i></div>
  </div>
  <div class="brand" style="left:86px;top:78px;width:94px;height:94px">Parkdale<br>Northly</div>
  <nav class="nav" style="left:612px;top:76px">
    <span>HOME</span><span>ABOUT US</span><span>OUR WORK</span><span>SERVICES</span><span>CONTACT US</span>
    <svg width="12" height="12" viewBox="0 0 12 12"><circle cx="5" cy="5" r="3.5" fill="none" stroke="#fff" stroke-width="2"/><path d="M8 8l3 3" stroke="#fff" stroke-width="2"/></svg>
  </nav>
  <div class="hero-art" role="img" aria-label="Chalk-style doodles of social media icons around the words social media"></div>
  <h1>WE ARE <span class="strong">EXPERT</span> in<br><span class="line2">SOCIAL MEDIA MARKETING!</span></h1>
  <div class="discover">
    <h3>DISCOVER OUR SERVICES</h3>
    <p class="small" style="font-size:12px">Lorem Ipsum has been the industry's standard dummy text ever since<br>the when an unknown printer.</p>
  </div>
  <div class="btn light" style="left:86px;top:416px;width:174px">EXPLORE MORE</div>
  <div class="btn ghost" style="left:268px;top:416px;width:174px">FREE SEO ANALYSIS</div>
  <div class="dots"><i class="on"></i><i></i><i></i><i></i></div>
</header>

<section>
  <h2 class="section-title" style="left:86px;top:616px">AMAZING <b>SERVICES</b></h2>
  <div class="rule" style="left:86px;top:658px;width:120px"></div>

  <div class="service" style="left:86px">
    <svg viewBox="0 0 48 48" width="48"><path d="M40 6c-10 0-18 6-22 16l8 8c10-4 16-12 16-22z" fill="#1c242e"/><path d="M16 24l-8 2 4-8 8-2zM24 32l-2 8 8-4 2-8z" fill="#1c242e"/><path d="M12 34l-6 8 8-6" stroke="#1c242e" stroke-width="3" fill="none"/></svg>
    <h4>CONTENT STRATEGY</h4><p class="small">It has survived not only five centuries<br>but also the leap into electronic.</p>
  </div>
  <div class="service" style="left:350px">
    <svg viewBox="0 0 48 48" width="48"><rect x="3" y="4" width="42" height="30" fill="none" stroke="#1c242e" stroke-width="3"/><rect x="8" y="9" width="32" height="20" fill="#1c242e" opacity=".15"/><path d="M18 34v6h12v-6M12 42h24" stroke="#1c242e" stroke-width="3" fill="none"/></svg>
    <h4>ONLINE MARKETING</h4><p class="small">It has survived not only five centuries<br>but also the leap into electronic.</p>
  </div>
  <div class="service" style="left:614px">
    <svg viewBox="0 0 48 48" width="48"><path d="M34 4l10 10L16 42H6V32z" fill="none" stroke="#1c242e" stroke-width="2.5"/><path d="M28 10l10 10M6 32l10 10" stroke="#1c242e" stroke-width="2.5"/></svg>
    <h4>BRAND IDENDITY</h4><p class="small">It has survived not only five centuries<br>but also the leap into electronic.</p>
  </div>
  <div class="service" style="left:878px">
    <svg viewBox="0 0 56 48" width="56"><g stroke="#1c242e" stroke-width="2" fill="none"><path d="M28 24L10 8M28 24L46 8M28 24L10 40M28 24L46 40"/><circle cx="28" cy="24" r="6" fill="#fff"/><circle cx="8" cy="6" r="5" fill="#fff"/><circle cx="48" cy="6" r="5" fill="#fff"/><circle cx="8" cy="42" r="5" fill="#fff"/><circle cx="48" cy="42" r="5" fill="#fff"/></g></svg>
    <h4>SEO &amp; SMM SERVICES</h4><p class="small">It has survived not only five centuries<br>but also the leap into electronic.</p>
  </div>
</section>

<section class="offer-band">
  <svg class="abs" style="left:0;top:0" width="1200" height="338" viewBox="0 0 1200 338"><path d="M0 110 Q600 -60 1200 110 V338 H0Z" fill="var(--navy)"/></svg>
  <div class="lead" style="top:36px;font-size:24px;font-weight:800">HIGHEST</div>
  <div class="rule" style="left:480px;top:52px;width:60px;background:#6b7580"></div>
  <div class="rule" style="left:660px;top:52px;width:60px;background:#6b7580"></div>
  <div class="lead" style="top:70px;font-size:21px">Performance! We’d like</div>
  <div class="lead" style="top:98px;font-size:21px">to help you find a solution to your challenges ...</div>
</section>

<div class="offer">
  <svg class="abs" style="left:0;top:0" width="862" height="145" viewBox="0 0 862 145"><path d="M0 0H550L460 145H0Z" fill="#e6e6e6"/></svg>
  <div class="abs head" style="left:28px;top:20px;font-size:50px;line-height:48px;color:var(--ink)">GET <i style="font-weight:800;font-size:38px">20% OFF</i><br><b style="font-weight:800">TODAY</b> <span style="font-size:42px;font-weight:300">|</span> <span style="font-size:12px;font-weight:700">ESTABLISHED FACT THAT</span></div>
  <div class="abs" style="left:556px;top:18px;width:260px">
    <p class="head" style="font-size:17px;font-weight:800">AFFORDABLE <span style="font-size:10px;font-weight:600;color:#666">Lorem Ipsum.</span></p>
    <p class="small" style="margin-top:4px">It has survived not only five centuries<br>but also the leap into electronic.</p>
  </div>
  <div class="btn" style="left:556px;top:92px;width:114px;height:29px;background:var(--ink);color:#fff;font-size:10px">VIEW DETAILS</div>
</div>

<section>
  <div class="photo" role="img" aria-label="Photograph of a professional boxer with red hand wraps" style="left:86px;top:1229px;width:414px;height:530px"></div>
  <div class="abs" style="left:86px;top:1671px;width:414px;height:88px;background:#000;color:#fff;text-align:center">
    <div class="head" style="font-size:34px;font-weight:700;letter-spacing:3px;margin-top:6px">Tom Harlow</div>
    <div class="head" style="display:inline-block;border:2px solid #fff;font-size:14px;font-weight:700;letter-spacing:8px;padding:1px 10px">PROFESSIONAL BOXER</div>
  </div>
  <div class="work-panel">
    <div class="abs head" style="left:39px;top:25px;background:var(--ink);color:#fff;font-size:25px;padding:2px 10px">OUR <b style="font-weight:800">WORK</b></div>
    <div class="abs" style="left:39px;top:82px;width:540px">
      <h4>THE PROBLEM</h4>
      <p class="small">Professional Boxer Tom Harlow approached Parkdale Northly to launch his personal-brand. Tom Harlow signed as a professional to Ringside Promotions &amp; Promoter Dale Mercer.</p>
      <h4 style="margin-top:22px">THE SOLUTION</h4>
      <p class="small">PKN launched Tom Harlow to the nation with a strategic plan first unveiling him to his home town at Ashford Rovers FC as a match day sponsor. We combined this by filming a documentary, cutting edge boxing promotional videos, photography and secured further sponsorship with our partners.</p>
      <p class="small" style="margin-top:20px">Parkdale Northly campaign tactics of mixing traditional and digital marketing has helped launch a successful boxing debut for the former the National Squad boxer. The campaign made a real lasting impact on Tom’s career by selling a record number of tickets. Our promotional videos and photography sparked real conversations on digital platforms giving the brand a chance to maintain its position.</p>
    </div>
    <div class="arrows" style="left:39px;top:439px"><i style="background:var(--ink);color:#fff">‹</i><i style="background:var(--ink);color:#fff">›</i></div>
  </div>
</section>

<section class="videos">
  <h2 class="section-title" style="left:86px;top:38px;color:#fff">POPULAR <b>VIDEOS</b></h2>
  <div class="rule" style="left:86px;top:80px;width:120px;background:#6b7580"></div>
  <div class="arrows" style="left:1043px;top:42px"><i style="background:#fff;color:var(--ink)">‹</i><i style="background:#fff;color:var(--ink)">›</i></div>

  <div class="video" style="left:86px">
    <div class="thumb" role="img" aria-label="Video still of a hand touching a tablet with floating icons" style="background:linear-gradient(135deg,#0d2a4a,#2f6fa8)"><em>02:57</em></div>
    <h4>CONTENT STRATEGY</h4><p class="small">It has survived not only five centuries but also the leap into electronic. It has survived not only five centuries but also the leap into electronic..</p>
  </div>
  <div class="video" style="left:438px">
    <div class="thumb" role="img" aria-label="Video still of social network app buttons on a screen" style="background:linear-gradient(135deg,#0a1626,#2b5a9a)"><em>14:20</em></div>
    <h4>CONTENT STRATEGY</h4><p class="small">It has survived not only five centuries but also the leap into electronic. It has survived not only five centuries but also the leap into electronic..</p>
  </div>
  <div class="video" style="left:788px">
    <div class="thumb" role="img" aria-label="Video still of colourful 3D letters on a wooden table" style="background:linear-gradient(135deg,#7a5a3a,#c08a50 50%,#6f9ac8)"><em>05:30</em></div>
    <h4>CONTENT STRATEGY</h4><p class="small">It has survived not only five centuries but also the leap into electronic. It has survived not only five centuries but also the leap into electronic..</p>
  </div>

  <div class="rule" style="left:86px;top:420px;width:1028px;background:#46505c"></div>
  <div class="btn" style="left:524px;top:454px;width:152px;height:44px;background:#fff;color:var(--ink);font-size:10px">SEE ALL VIDEOS</div>
</section>

<section>
  <svg class="abs" style="left:545px;top:2385px" width="110" height="110" viewBox="0 0 110 110"><circle cx="48" cy="48" r="36" fill="none" stroke="#f0f0f0" stroke-width="14"/><path d="M74 74l28 28" stroke="#f0f0f0" stroke-width="16"/></svg>
  <div class="lead" style="top:2406px;color:var(--ink);font-size:26px;font-weight:400">RECEIVE YOUR FREE SEO REPORT BEST</div>
  <div class="lead" style="top:2438px;color:var(--ink);font-size:26px"><b style="font-weight:800;font-size:32px">ANALYSIS</b> NOW</div>
  <div class="abs" style="left:174px;top:2502px;width:702px;height:49px;background:var(--field);border:1px solid #ddd;font-size:13px;color:#666;padding:16px 20px;font-weight:600">Search here</div>
  <div class="btn" style="left:876px;top:2502px;width:152px;height:49px;background:var(--navy);color:#fff;font-size:10px">CHECK</div>
</section>

<footer class="footer">
  <div class="brand" style="left:553px;top:43px;width:94px;height:96px">Parkdale<br>Northly</div>
  <nav class="nav" style="left:376px;top:170px;font-size:12px;gap:30px">
    <span>HOME</span><span>ABOUT US</span><span>OUR WORK</span><span>SERVICES</span><span>CONTACT US</span>
  </nav>
  <div class="social" style="left:520px;top:225px;gap:22px"><i></i><i></i><i></i><i></i><i></i></div>
  <div class="rule" style="left:86px;top:280px;width:1028px;background:#3c4652"></div>
  <div class="lead" style="top:296px;font-size:12px;font-family:'Open Sans',Arial,sans-serif;font-weight:600">Copyright- 2018, <b>Parkdale Northly</b> All Right Reserved</div>
  <div class="abs" style="left:1067px;top:258px;width:48px;height:48px;border-radius:50%;background:#fff;display:flex;align-items:center;justify-content:center">
    <svg width="14" height="10" viewBox="0 0 14 10"><path d="M1 8l6-6 6 6" stroke="var(--navy)" stroke-width="2.5" fill="none"/></svg>
  </div>
</footer>

</body>
</html>
```